Business Card Design

We need the business card for our new business based in St. Marys, we manufacture mainly bubble wraps. And we would like the design to use our company logo and also make it easy for people to understand right away we are bubble wrap manufacturer

Industry/Entity Type

Business

Contact Information for Business Card

Cushora Pty Ltd, 14 Harlow Lane St. Marys NSW 2760, Tel: 02 9481 5726, Fax: 9481 5739, Dao Lin, General Manager, Mobile :0427 315 640, dao.lin@cushora.com.au, Website: cushora.com.au

```html
<!DOCTYPE html>
<html lang="en">
<head>
<meta charset="utf-8">
<title>Cushora Pty Ltd – Business Card</title>
<link rel="stylesheet" href="https://fonts.googleapis.com/css2?family=Exo+2:wght@300;400;600;700&display=swap">
<style>
  :root {
    --page: #ecebe8;
    --card: #ffffff;
    --card-edge: #e2e2e2;
    --ink-dark: #4a4a4a;
    --ink: #6b6b6b;
    --ink-soft: #8d8d8d;
    --accent: #d8343a;
    --band-rule: #b9b9b9;
    --band-light: #f4f4f4;
    --band-mid: #dcdcdc;
    --band-dark: #b8b8b8;
  }
  * { box-sizing: border-box; margin: 0; padding: 0; }
  html, body {
    width: 1200px; height: 885px; overflow: hidden;
    background: var(--page);
    font-family: "Exo 2", sans-serif;
  }
  .canvas {
    width: 1200px; height: 885px;
    display: flex; align-items: center; justify-content: center; gap: 48px;
  }
  .card {
    width: 540px; height: 330px;
    background: var(--card);
    border: 1px solid var(--card-edge);
    box-shadow: 0 6px 18px rgba(0,0,0,.12);
    position: relative;
    overflow: hidden;
  }

  /* Front */
  .card-front__head {
    height: 132px; position: relative;
    padding: 34px 30px 0 30px;
  }
  .brand__name {
    font-weight: 700; font-size: 46px; letter-spacing: 2px;
    color: var(--ink-dark); line-height: 1;
  }
  .brand__tagline {
    margin-top: 10px;
    font-weight: 400; font-size: 11px; letter-spacing: 3.2px;
    color: var(--ink-soft); text-transform: uppercase;
  }
  .person {
    position: absolute; top: 26px; right: 30px; text-align: right;
  }
  .person__name { font-weight: 600; font-size: 21px; color: var(--accent); line-height: 1.1; }
  .person__role { font-weight: 400; font-size: 15px; color: var(--ink); margin-top: 3px; }
  .person__email { font-weight: 300; font-size: 12.5px; color: var(--ink); margin-top: 6px; }

  .product-band {
    height: 128px;
    border-top: 6px solid var(--band-rule);
    border-bottom: 6px solid var(--band-rule);
    background:
      radial-gradient(ellipse at 70% 30%, var(--band-light) 0%, transparent 55%),
      linear-gradient(180deg, var(--band-light) 0%, var(--band-mid) 60%, var(--band-dark) 100%);
  }

  .contact-row {
    height: 70px;
    display: flex; align-items: center; justify-content: space-between;
    padding: 0 30px;
  }
  .contact {
    display: flex; align-items: center; gap: 8px;
    font-weight: 400; font-size: 17px; color: var(--ink);
  }
  .contact__icon { width: 16px; height: 16px; flex: none; }
  .contact-row__divider { width: 1px; height: 20px; background: var(--band-rule); }

  /* Back */
  .card-back {
    display: flex; align-items: center; justify-content: center; gap: 18px;
  }
  .card-back__rule { width: 70px; height: 1px; background: var(--ink-soft); }
  .card-back__web { font-weight: 400; font-style: normal; font-size: 24px; color: var(--ink); letter-spacing: .5px; }
</style>
</head>
<body>
<main class="canvas">
  <section class="card card-front" aria-label="Business card front">
    <header class="card-front__head">
      <div class="brand">
        <div class="brand__name">CUSHORA</div>
        <div class="brand__tagline">Protective Packaging Solutions</div>
      </div>
      <div class="person">
        <div class="person__name">Dao Lin</div>
        <div class="person__role">General Manager</div>
        <div class="person__email">dao.lin@cushora.com.au</div>
      </div>
    </header>

    <div class="product-band" role="img" aria-label="Close-up photograph of clear bubble wrap"></div>

    <footer class="contact-row">
      <div class="contact">
        <svg class="contact__icon" viewBox="0 0 16 16" aria-hidden="true">
          <rect width="16" height="16" rx="2" fill="var(--accent)"/>
          <path d="M4 6c0-1.5 1.8-2.4 4-2.4S12 4.5 12 6h-2.2V5.2H6.2V6zM5 7.2h6l.8 4.8H4.2z" fill="#fff"/>
        </svg>
        <span>02 9481 5726</span>
      </div>
      <span class="contact-row__divider"></span>
      <div class="contact">
        <svg class="contact__icon" viewBox="0 0 16 16" aria-hidden="true">
          <rect width="16" height="16" rx="2" fill="var(--accent)"/>
          <rect x="4" y="3" width="8" height="4" fill="#fff"/>
          <rect x="3" y="7.5" width="10" height="5.5" rx="1" fill="#fff"/>
          <rect x="5" y="9.2" width="6" height="1" fill="var(--accent)"/>
        </svg>
        <span>9481 5739</span>
      </div>
      <span class="contact-row__divider"></span>
      <div class="contact">
        <svg class="contact__icon" viewBox="0 0 16 16" aria-hidden="true">
          <rect width="16" height="16" rx="2" fill="var(--accent)"/>
          <rect x="4.5" y="2.5" width="7" height="11" rx="1" fill="#fff"/>
          <rect x="5.7" y="4" width="4.6" height="6.5" fill="var(--accent)"/>
        </svg>
        <span>0427 315 640</span>
      </div>
    </footer>
  </section>

  <section class="card card-back" aria-label="Business card back">
    <span class="card-back__rule"></span>
    <span class="card-back__web">cushora.com.au</span>
    <span class="card-back__rule"></span>
  </section>
</main>
</body>
</html>
```